Business Cards using attached files

Please make new business cards using files attached. I would like something a little more updated possibly. Double sided.
I am wanting to make sure I can change the names and positions easily myself.

Target Market(s)

Automotive Repair

Industry/Entity Type

Automotive

Contact Information for Business Card

See attached files

Font styles to use
Serif

Colors
0054AA
0677BA
7BADD7
CADEEF
E8F1F8

Requirements
Must have
• Red white blue colors
Nice to have
• I'd like it slightly updated from our existing design. Double sided. I'd like to be able to change names and positions easily to have them printed.
Should not have
• I'm not sure

```html
<!DOCTYPE html>
<html lang="en">
<head>
<meta charset="utf-8">
<title>Brookline Auto – Business Cards</title>
<link rel="stylesheet" href="https://fonts.googleapis.com/css2?family=Montserrat:wght@400;500;600;700&family=Oswald:wght@500;600&display=swap">
<style>
  :root {
    --navy: #0b3c60;
    --navy-deep: #072f4d;
    --red: #e8282e;
    --ink: #1d1d1f;
    --white: #ffffff;
    --paper: #f4f4f4;
    --backdrop: #d9dadc;
  }
  * { box-sizing: border-box; margin: 0; padding: 0; }
  html, body { width: 1200px; height: 1200px; overflow: hidden; }
  body {
    background: var(--backdrop);
    font-family: "Montserrat", Arial, sans-serif;
    position: relative;
  }
  .card {
    position: absolute;
    left: 180px;
    width: 840px;
    height: 480px;
    border-radius: 30px;
    overflow: hidden;
    box-shadow: 0 10px 28px rgba(0,0,0,0.22);
  }
  /* Front */
  .card-front {
    top: 90px;
    background: linear-gradient(180deg, var(--white) 0%, var(--paper) 100%);
  }
  .identity {
    position: absolute;
    left: 62px;
    top: 150px;
    padding-left: 18px;
    border-left: 6px solid var(--red);
  }
  .identity-name {
    color: var(--red);
    font-weight: 600;
    font-size: 34px;
    line-height: 1;
    letter-spacing: 0.5px;
  }
  .identity-title {
    color: var(--ink);
    font-weight: 500;
    font-size: 21px;
    line-height: 1.1;
    margin-top: 4px;
    letter-spacing: 0.5px;
  }
  .contact-list {
    position: absolute;
    left: 82px;
    top: 236px;
    list-style: none;
    font-size: 21px;
    color: var(--ink);
    line-height: 1.3;
  }
  .contact-list li { display: flex; align-items: flex-start; gap: 16px; }
  .contact-icon { width: 24px; height: 24px; flex: none; margin-top: 3px; fill: var(--red); }
  .brand-mark {
    position: absolute;
    right: 60px;
    top: 80px;
    display: flex;
    align-items: center;
    gap: 14px;
  }
  .brand-dot { width: 26px; height: 26px; border-radius: 50%; background: var(--red); }
  .brand-name {
    font-weight: 700;
    font-size: 40px;
    color: var(--navy);
  }
  .service-line {
    position: absolute;
    left: 0;
    right: 0;
    bottom: 40px;
    text-align: center;
    font-family: "Oswald", "Arial Narrow", sans-serif;
    font-weight: 600;
    font-size: 22px;
    color: var(--navy);
    letter-spacing: 0.3px;
    white-space: nowrap;
  }
  .service-line .sep { color: #9aa7b3; font-weight: 500; margin: 0 5px; }
  .front-strip { position: absolute; left: 0; bottom: 0; width: 840px; height: 26px; }
  /* Back */
  .card-back {
    top: 630px;
    background: radial-gradient(ellipse at 50% 42%, #15527d 0%, var(--navy) 55%, var(--navy-deep) 100%);
  }
  .back-badge {
    position: absolute;
    left: 50%;
    top: 70px;
    transform: translateX(-50%);
    display: flex;
    align-items: center;
    gap: 18px;
  }
  .back-badge .brand-dot { width: 36px; height: 36px; }
  .back-badge .brand-name { color: var(--white); font-size: 64px; }
  .tagline {
    position: absolute;
    left: 0;
    right: 0;
    bottom: 90px;
    text-align: center;
    color: var(--white);
    font-weight: 600;
    font-size: 30px;
    letter-spacing: 0.5px;
  }
</style>
</head>
<body>

<section class="card card-front" aria-label="Business card front">
  <div class="brand-mark">
    <span class="brand-dot"></span>
    <span class="brand-name">Brookline Auto</span>
  </div>

  <div class="identity">
    <p class="identity-name">DANIEL VERANO</p>
    <p class="identity-title">GENERAL MANAGER</p>
  </div>

  <ul class="contact-list">
    <li>
      <svg class="contact-icon" viewBox="0 0 24 24" aria-hidden="true"><path d="M6.6 10.8a15.1 15.1 0 0 0 6.6 6.6l2.2-2.2c.3-.3.7-.4 1-.2 1.1.4 2.3.6 3.6.6.6 0 1 .4 1 1V20c0 .6-.4 1-1 1A17 17 0 0 1 3 4c0-.6.4-1 1-1h3.5c.6 0 1 .4 1 1 0 1.3.2 2.5.6 3.6.1.3 0 .7-.2 1z"/></svg>
      <span>(555) 201-4410</span>
    </li>
    <li>
      <svg class="contact-icon" viewBox="0 0 24 24" aria-hidden="true"><path d="M6 2h10l2 2v5H6zM3 10h18v10H3zm3 3v2h3v-2zm5 0v2h3v-2zm5 0v2h2v-2zm-10 4v1h12v-1z"/></svg>
      <span>(555) 201-4411</span>
    </li>
    <li>
      <svg class="contact-icon" viewBox="0 0 24 24" aria-hidden="true"><path d="M2 5h20v14H2zm2 2v.5l8 5.5 8-5.5V7l-8 5.3z"/></svg>
      <span>dan@brooklineauto.com</span>
    </li>
    <li>
      <svg class="contact-icon" viewBox="0 0 24 24" aria-hidden="true"><path d="M12 2a7 7 0 0 0-7 7c0 5 7 13 7 13s7-8 7-13a7 7 0 0 0-7-7zm0 4a3 3 0 1 1 0 6 3 3 0 0 1 0-6z"/></svg>
      <span>48 Millbrook Road<br>Eastfield, NY 10040</span>
    </li>
  </ul>

  <p class="service-line">AUTO SERVICE<span class="sep">|</span>INSPECTIONS<span class="sep">|</span>LUBE/OIL SERVICE<span class="sep">|</span>DIESEL<span class="sep">|</span>FLEET<span class="sep">|</span>DOT<span class="sep">|</span>TRUCK<span class="sep">|</span>TRAILER</p>

  <svg class="front-strip" viewBox="0 0 840 26" preserveAspectRatio="none" aria-hidden="true">
    <polygon points="0,12 470,12 470,26 0,26" fill="#e8282e"/>
    <polygon points="480,0 840,0 840,26 480,26" fill="#0b3c60"/>
  </svg>
</section>

<section class="card card-back" aria-label="Business card back">
  <div class="back-badge">
    <span class="brand-dot"></span>
    <span class="brand-name">Brookline Auto</span>
  </div>
  <p class="tagline">Family Owned &amp; Operated Since 1991</p>
</section>

</body>
</html>
```